Cover for a book about building companies without hierarchy

We need to design the cover of our new book. In 2018 we have developed a new organizational design called "Brevunt" which mean equal, just in Latin. This organizational design is hierarchy-free, and it is formed by a radial network of self-organizing teams, where people can take decisions pertaining their job, be autonomous, and contribute to the well being of the larger organization. We published a book in 2018 (see the cover attached), titled: "Brevunt. The Open People-first Operating Model to Flourish in an Uncertain Age", where we used the graphic representation of the Brevunt structure in the cover (see attached). The book is intended for top managers, entrepreneurs, businesses.
After 5 years from its launch, we implemented this design in a number of companies and we learned a lot about what works and the challenges. So we decided to publish another book that will be titled: "Brevunt. 5 rules to build a people-first office" where we present a revised model, we focus on the principles behind Brevunt and we tell the story of the implementation of Brevunt in Caffora Italy.
The book cover design must include both front and back, using the template attached.
In the front we need to include: an image or illustration, the Names of the authors (Lucrezia Manfretti and Marcello Vagni) and the Quolvane logo.
In the back we shall include: an empty space for the ISDN code as in the template, a short description of the book, the pictures and short bios of the authors .
In the spine we shall include: the title and authors.
Here's the bios:
Lucrezia Manfretti is a partner at Quolvane, a global organizational development firm, a former executive in the corporate setting (including Brindle & Holloway and Zimbu! Inc.) and Past President of GTN Global (Global Tutoring Network). She is the author of the book “Inner Compass. The Road to Renewing Guidance” and a LUMIx speaker.
Marcello Vagni is a partner at Quolvane and a former manager in multinational settings. He is the co-author of the Keswick Management Quarterly articles “Why Your Inner Mood Shapes your Daily Output”, “3 Ways to Lift a Gloomy Day”, “Preparing Your Thoughts Properly for a Long Break” and “An Easy Method to Ease Lasting Tension”.
Pictures of the authors attached.
The final versions of the book cover shall be:
- book cover for paperback in English (front and back)
- Book cover for paperback in Italian (front and back)
- Book cover for kindle (only front)

```html
<!DOCTYPE html>
<html lang="en">
<head>
<meta charset="utf-8">
<title>Brevunt — Book Cover</title>
<link href="https://fonts.googleapis.com/css2?family=Comfortaa:wght@400&family=Oswald:wght@200;600&display=swap" rel="stylesheet">
<style>
  :root {
    --page-bg: #ffffff;
    --cover-bg: #050507;
    --title-orange: #e8582c;
    --text-white: #f4f4f4;
    --tree-red: #d0201f;
    --net-blue: #1c3a78;
    --net-teal: #1a6f7a;
  }
  html, body {
    margin: 0;
    padding: 0;
    width: 1200px;
    height: 1042px;
    overflow: hidden;
    background: var(--page-bg);
  }
  .canvas {
    position: relative;
    width: 1200px;
    height: 1042px;
  }
  .cover {
    position: absolute;
    left: 273px;
    top: 31px;
    width: 654px;
    height: 980px;
    background: var(--cover-bg);
    overflow: hidden;
  }
  .cover-art {
    position: absolute;
    left: 0;
    top: 300px;
    width: 654px;
    height: 680px;
    background:
      radial-gradient(ellipse 40% 70% at 50% 100%, rgba(208,32,31,0.85) 0%, rgba(208,32,31,0.25) 40%, transparent 70%),
      radial-gradient(ellipse 55% 35% at 25% 30%, rgba(200,60,80,0.45) 0%, transparent 70%),
      radial-gradient(ellipse 45% 35% at 78% 35%, rgba(26,111,122,0.5) 0%, transparent 70%),
      radial-gradient(ellipse 70% 45% at 50% 35%, rgba(28,58,120,0.55) 0%, transparent 75%),
      var(--cover-bg);
  }
  .title {
    position: absolute;
    left: 0;
    right: 0;
    top: 38px;
    margin: 0;
    text-align: center;
    font-family: "Comfortaa", sans-serif;
    font-weight: 400;
    font-size: 128px;
    line-height: 1;
    letter-spacing: 2px;
    color: var(--title-orange);
  }
  .subtitle {
    position: absolute;
    left: 0;
    right: 0;
    top: 188px;
    margin: 0;
    text-align: center;
    font-family: "Oswald", sans-serif;
    font-weight: 200;
    font-size: 38px;
    line-height: 44px;
    letter-spacing: 1px;
    color: var(--text-white);
    text-transform: uppercase;
  }
  .authors {
    position: absolute;
    left: 0;
    right: 0;
    top: 905px;
    margin: 0;
    text-align: center;
    font-family: "Oswald", sans-serif;
    font-weight: 600;
    font-size: 24px;
    letter-spacing: 3px;
    color: var(--text-white);
    text-transform: uppercase;
  }
</style>
</head>
<body>
  <div class="canvas">
    <section class="cover">
      <div class="cover-art" role="img" aria-label="Illustration of a glowing red tree whose branches spread into a colourful digital network of scattered pixels on black"></div>
      <h1 class="title">brevunt</h1>
      <p class="subtitle">5 Rules to Build<br>A People-First Office</p>
      <p class="authors">Lucrezia Manfretti - Marcello Vagni</p>
    </section>
  </div>
</body>
</html>
```